Larkspur Ridge Management - Business Cards

I need business cards. My current logo was designed by a designer at this site and I very much like and am happy with the results. I would like a business card that is trendy, unique, current yet professional. I deal with high net worth clients daily

Target Market(s)

Out of state investors looking to get into the rental market in Ohio

Industry/Entity Type

Property Management, Consulting

Contact Information for Business Card

Name, Title (Chief Financial Officer) office phone number (555) 817-3094 website address larkridgemgmt.example

Font styles to use
Sans Serif

Colors
0054AA
0677BA
7BADD7
CADEEF
E8F1F8
0094D4
00A9DD
6FCCEA
C7EBF8
E9F6FB
00AB8E
00BBA5
67D7C9
C6EFE9
E9F9F6

```html
<!DOCTYPE html>
<html lang="en">
<head>
<meta charset="utf-8">
<title>Larkspur Ridge Management – Business Cards</title>
<link href="https://fonts.googleapis.com/css2?family=Poppins:wght@400;500;600;700&display=swap" rel="stylesheet">
<style>
  :root {
    --backdrop: #19223a;
    --card-white: #ffffff;
    --navy: #22335a;
    --navy-ink: #2a3153;
    --maroon: #5e2c47;
    --red: #cc2a31;
    --red-deep: #a01622;
    --text-light: #ffffff;
  }
  * { margin: 0; padding: 0; box-sizing: border-box; }
  html, body {
    width: 1200px; height: 1200px; overflow: hidden;
    background: var(--backdrop);
    font-family: "Poppins", sans-serif;
  }
  .stage { position: relative; width: 1200px; height: 1200px; }
  .card {
    position: absolute; left: 227px; width: 745px; height: 426px;
    border-radius: 10px; overflow: hidden; background: var(--card-white);
  }
  .card--front { top: 147px; }
  .card--back { top: 628px; }
  .card__art { position: absolute; inset: 0; width: 745px; height: 426px; }
  .tagline {
    position: absolute; left: 515px; top: 157px;
    color: var(--text-light); font-size: 21px; font-weight: 400;
    line-height: 35.5px; letter-spacing: 0.3px;
  }
  .brand {
    position: absolute; left: 40px; top: 150px; width: 300px;
    display: flex; flex-direction: column; align-items: center; gap: 14px;
  }
  .brand__dot { width: 34px; height: 34px; border-radius: 50%; background: var(--red); }
  .brand__name {
    color: var(--navy); font-weight: 700; font-size: 27px;
    line-height: 32px; text-align: center; letter-spacing: 0.3px;
  }
  .contact { position: absolute; left: 80px; top: 140px; color: var(--navy-ink); }
  .contact__name { font-size: 30px; font-weight: 600; line-height: 38px; letter-spacing: 0.2px; }
  .contact__title { font-size: 14px; font-weight: 400; margin-top: 2px; }
  .contact__row {
    display: flex; align-items: center; gap: 14px;
    font-size: 18.5px; font-weight: 600; color: var(--navy);
  }
  .contact__row--phone { margin-top: 20px; }
  .contact__row--web { margin-top: 17px; }
  .contact__icon { width: 18px; height: 18px; flex: none; }
</style>
</head>
<body>
<main class="stage">

  <section class="card card--front" aria-label="Card front">
    <svg class="card__art" viewBox="0 0 745 426" aria-hidden="true">
      <defs>
        <linearGradient id="front-panel" x1="1" y1="0" x2="0.3" y2="1">
          <stop offset="0.35" stop-color="#22335a"/>
          <stop offset="1" stop-color="#5e2c47"/>
        </linearGradient>
      </defs>
      <polygon points="188,0 745,0 745,426 430,426 430,137" fill="url(#front-panel)"/>
      <polygon points="188,0 256,0 458,117 430,137" fill="var(--red-deep)"/>
      <polygon points="430,137 458,117 458,385 430,385" fill="var(--red)"/>
    </svg>
    <div class="brand">
      <span class="brand__dot"></span>
      <p class="brand__name">Larkspur Ridge<br>Management</p>
    </div>
    <p class="tagline">Property<br>Management<br>&amp; Consulting</p>
  </section>

  <section class="card card--back" aria-label="Card back">
    <svg class="card__art" viewBox="0 0 745 426" aria-hidden="true">
      <defs>
        <linearGradient id="back-panel" x1="0.2" y1="0.1" x2="1" y2="1">
          <stop offset="0.3" stop-color="#22335a"/>
          <stop offset="1" stop-color="#5e2c47"/>
        </linearGradient>
      </defs>
      <polygon points="456,0 745,0 745,426 696,426 456,288" fill="url(#back-panel)"/>
      <polygon points="427,308 456,288 696,426 628,426" fill="var(--red-deep)"/>
      <polygon points="427,39 456,39 456,288 427,308" fill="var(--red)"/>
    </svg>
    <div class="contact">
      <h1 class="contact__name">Daniel Whitford</h1>
      <p class="contact__title">Chief Financial Officer</p>
      <p class="contact__row contact__row--phone">
        <svg class="contact__icon" viewBox="0 0 24 24" aria-hidden="true">
          <path d="M6.6 10.8a15.1 15.1 0 0 0 6.6 6.6l2.2-2.2a1 1 0 0 1 1-.25 11.4 11.4 0 0 0 3.6.57 1 1 0 0 1 1 1V20a1 1 0 0 1-1 1A17 17 0 0 1 3 4a1 1 0 0 1 1-1h3.5a1 1 0 0 1 1 1c0 1.25.2 2.45.57 3.57a1 1 0 0 1-.25 1z" fill="var(--red)"/>
        </svg>
        (555) 817-3094
      </p>
      <p class="contact__row contact__row--web">
        <svg class="contact__icon" viewBox="0 0 24 24" aria-hidden="true">
          <circle cx="12" cy="12" r="9" fill="none" stroke="var(--red)" stroke-width="2.4"/>
          <path d="M3 12h18M12 3c3 3.2 3 14.8 0 18M12 3c-3 3.2-3 14.8 0 18" fill="none" stroke="var(--red)" stroke-width="2"/>
        </svg>
        www.larkridgemgmt.example
      </p>
    </div>
    <p class="tagline">Serving Out of<br>State Real Estate<br>Investors</p>
  </section>

</main>
</body>
</html>
```